Web Site Design

We need to design the whole web site for our small start up. We sell hospitality and culinary art internships abroad. I did my own design with WIX which is horrible meanwhile I started with my business. You can see it www.brightvoyage-intern.example I will need you to create a new and attractive web site and to leave it working on wix. The internship destinations are United Arab Emirates, Thailand, China, Spain, Brazil and maybe leave a couple of pages for future destinations.You could also get other ideas of other sites that do internships.

Target Market(s)

Students and recent graduates of hospitality and culinary art majors

Industry/Entity Type

Education

Number of Pages Required

5+ page

Requirements
Must have
• Addittional to our program destinations, or to the pages in the current site. The website must contain a page for Universities or Hotels who require our service

```html
<!DOCTYPE html>
<html lang="en">
<head>
<meta charset="utf-8">
<title>BrightVoyage – Hospitality Internship Program</title>
<link rel="stylesheet" href="https://fonts.googleapis.com/css2?family=Montserrat:wght@400;500;700;800&family=Open+Sans:wght@400;600&display=swap">
<style>
:root{
  --teal:#1d6f72;
  --teal-dark:#175c5f;
  --teal-line:#1f7477;
  --ink:#222;
  --text:#444;
  --grey:#ededed;
  --grey-dark:#e4e4e4;
  --footer:#1b6a6d;
  --white:#fff;
  --black:#111;
}
*{margin:0;padding:0;box-sizing:border-box}
html,body{width:1200px;height:2844px;overflow:hidden}
body{position:relative;background:var(--white);font-family:"Open Sans",Arial,sans-serif;color:var(--text)}
.abs{position:absolute}
.heading{font-family:"Montserrat",Arial,sans-serif;font-size:42px;color:var(--teal);text-align:center;width:1200px;left:0;letter-spacing:0.5px}
.heading b{font-weight:800}
.heading span{font-weight:400}
.vline{position:absolute;left:599px;width:2px;background:var(--teal-line)}
.btn{position:absolute;display:flex;align-items:center;justify-content:center;background:var(--teal);color:var(--white);border-radius:22px;font-family:"Montserrat",Arial,sans-serif;font-size:14px;font-weight:500}

/* header */
.site-header{top:0;left:0;width:1200px;height:74px;background:var(--white)}
.brand-box{top:0;left:133px;width:142px;height:100px;background:var(--black);display:flex;flex-direction:column;align-items:center;justify-content:center;gap:6px;z-index:3}
.brand-box .dot{width:30px;height:30px;border:2px solid var(--white);border-radius:50%}
.brand-name{font-family:"Montserrat",Arial,sans-serif;font-size:15px;font-weight:500;color:var(--white);letter-spacing:1px;text-transform:uppercase}
.main-nav{top:26px;left:423px;display:flex;gap:0;font-family:"Montserrat",Arial,sans-serif;font-size:15px;color:#555}
.main-nav a{position:absolute;white-space:nowrap;text-decoration:none;color:#555}
.main-nav a.active{color:var(--teal)}
.nav-mail{display:flex;align-items:center;gap:7px}

/* hero */
.hero{top:74px;left:0;width:1200px;height:540px;overflow:hidden}
.hero-left{left:0;top:0;width:600px;height:540px;background:linear-gradient(135deg,#3f8c8f,#2b7b7e 60%,#1e6a6d)}
.hero-right{left:600px;top:0;width:600px;height:540px;background:linear-gradient(160deg,#d9d3c9,#9a8f84 45%,#2c2f35 80%)}
.hero-title{top:220px;left:0;width:1200px;text-align:center;font-family:"Montserrat",Arial,sans-serif;font-weight:700;font-size:40px;line-height:48px;color:var(--white);letter-spacing:0.5px}
.book-tab{top:244px;left:0;width:108px;height:52px;background:var(--black);color:var(--white);font-size:15px;display:flex;align-items:center;justify-content:center}
.scroll-cue{top:386px;left:584px}

/* about */
.about-frame{top:766px;left:133px;width:328px;height:328px;border:2px solid var(--teal)}
.about-photo{top:827px;left:182px;width:330px;height:330px;background:linear-gradient(135deg,#f4efe4,#c9b9a1 40%,#4a4440 85%)}
.about-text{top:868px;left:601px;width:470px;font-size:12.5px;line-height:20px;color:#555}

/* what we do */
.services{top:1229px;left:0;width:1200px;height:506px;background:var(--grey)}
.services-right{left:600px;top:0;width:600px;height:506px;background:var(--grey-dark)}
.service{position:absolute;width:220px;text-align:center}
.service svg{display:block;margin:0 auto}
.service h3{margin-top:12px;font-family:"Montserrat",Arial,sans-serif;font-weight:500;font-size:19px;color:var(--teal);text-transform:uppercase}
.service p{margin-top:10px;font-size:12.5px;line-height:19px;color:#555}

/* testimonials */
.quote{top:1884px;left:260px;width:680px;text-align:center;font-size:17.5px;line-height:28px;color:#555}
.author{top:1982px;left:0;width:1200px;text-align:center;font-family:"Montserrat",Arial,sans-serif;font-size:17px;color:var(--teal)}
.dots{top:2052px;left:570px;display:flex;gap:15px}
.dots i{width:9px;height:9px;border-radius:50%;background:#aaa;display:block}
.dots i.on{background:var(--teal)}

/* call to action */
.cta{top:2144px;left:0;width:1200px;height:507px;background:linear-gradient(180deg,#a7d4d4,#b9dddc 50%,#c3e2e1)}
.cta-text{top:2298px;left:260px;width:680px;text-align:center;font-size:17px;line-height:28px;color:#2a3b3c}
.socials{top:2530px;left:500px;width:200px;display:flex;justify-content:space-between}
.socials i{display:block;width:22px;height:22px;background:var(--teal-dark);border-radius:3px}

/* footer */
.site-footer{top:2651px;left:0;width:1200px;height:193px;background:var(--footer);color:var(--white)}
.footer-brand{top:26px;left:113px;width:160px;display:flex;flex-direction:column;align-items:center;gap:8px}
.footer-brand .dot{width:34px;height:34px;border:2px solid var(--white);border-radius:50%}
.divider{top:28px;width:1px;height:80px;background:rgba(255,255,255,.6)}
.contacts{font-size:12.5px;line-height:24.5px}
.copyright{top:146px;left:0;width:1200px;text-align:center;font-size:12.5px}
.chat{top:145px;left:859px;width:292px;height:48px;background:var(--black);display:flex;align-items:center;justify-content:space-between;padding:0 18px;font-family:"Montserrat",Arial,sans-serif;font-size:15px}
.chat-tag{top:163px;left:1166px;font-size:11px}
</style>
</head>
<body>

<header class="abs site-header">
  <nav class="abs main-nav">
    <a class="active" style="left:0">Welcome</a>
    <a style="left:108px">Programs</a>
    <a style="left:216px">Destinations</a>
    <a style="left:342px">Contact</a>
    <a class="nav-mail" style="left:433px">
      <svg width="14" height="11" viewBox="0 0 14 11"><rect width="14" height="11" fill="#333"/><path d="M0 0 7 6 14 0" stroke="#fff" stroke-width="1.4" fill="none"/></svg>
      info@brightvoyage-intern.example</a>
  </nav>
</header>

<div class="abs brand-box"><span class="dot"></span><span class="brand-name">BrightVoyage</span></div>

<section class="abs hero">
  <div class="abs hero-left" role="img" aria-label="Hotel reception desk photo with teal overlay"></div>
  <div class="abs hero-right" role="img" aria-label="Photo of two smiling front office staff at a hotel reception"></div>
  <h1 class="abs hero-title">HOSPITALITY INTERNSHIP<br>PROGRAM</h1>
  <div class="abs book-tab">Book Now</div>
  <svg class="abs scroll-cue" width="32" height="54" viewBox="0 0 32 54"><rect x="1" y="1" width="30" height="52" rx="15" fill="none" stroke="#fff" stroke-width="2"/><path d="M16 14v22M9 29l7 8 7-8" fill="none" stroke="#fff" stroke-width="2.5"/></svg>
</section>

<div class="vline" style="top:614px;height:65px"></div>
<h2 class="abs heading" style="top:710px"><b>ABOUT</b> <span>US</span></h2>
<div class="abs about-frame"></div>
<div class="abs about-photo" role="img" aria-label="Photo of a waitress serving coffee from a tray"></div>
<p class="abs about-text">Fusce sollicitudin lorem et luctus volutpat. Proin placerat dapibus gravida. In tristique tristique nulla eget hendrerit. Maecenas vel tortor accumsan quam varius imperdiet vel eget elit. Aenean facilisis tincidunt lectus, id dictum nisl luctus eget. Vivamus efficitur ex condimentum, malesuada eros eget, feugiat nibh. Sed tellus ex, imperdiet eget gravida sit amet, volutpat eget turpis. In nec ultricies est.</p>
<div class="btn" style="top:1005px;left:601px;width:124px;height:41px">Read More</div>

<section class="abs services">
  <div class="abs services-right"></div>
  <div class="vline" style="top:0;height:64px"></div>
  <h2 class="abs heading" style="top:84px"><b>WHAT</b> <span>WE DO</span></h2>

  <div class="service" style="left:133px;top:180px">
    <svg width="64" height="66" viewBox="0 0 64 66" fill="none" stroke="#1d6f72" stroke-width="2.5"><path d="M16 38c-9 0-13-8-9-14 3-5 9-5 11-3 1-8 8-12 14-12s13 4 14 12c2-2 8-2 11 3 4 6 0 14-9 14"/><path d="M16 38v14h32V38"/><path d="M16 58h32"/><path d="M26 44v8M32 44v8M38 44v8"/></svg>
    <h3>Culinary</h3><p>Maecenas vel tortor accumsan quam varius imperdiet vel eget elit</p></div>
  <div class="service" style="left:371px;top:180px">
    <svg width="64" height="66" viewBox="0 0 64 66" fill="none" stroke="#1d6f72" stroke-width="2.5"><path d="M18 4h8v12l6 8v38H12V24l6-8z"/><path d="M12 36h20M12 50h20"/><path d="M38 30h20c0 12-4 18-10 18s-10-6-10-18z"/><path d="M48 48v14M40 62h16"/></svg>
    <h3>F&amp;B</h3><p>Maecenas vel tortor accumsan quam varius imperdiet vel eget elit</p></div>
  <div class="service" style="left:609px;top:180px">
    <svg width="90" height="66" viewBox="0 0 90 66" fill="none" stroke="#1d6f72" stroke-width="2.5"><circle cx="45" cy="8" r="4"/><path d="M12 52c0-20 15-38 33-38s33 18 33 38"/><path d="M4 54h82v6H4z"/><path d="M24 34c4-8 10-12 16-13"/></svg>
    <h3>Front Office</h3><p>Maecenas vel tortor accumsan quam varius imperdiet vel eget elit</p></div>
  <div class="service" style="left:846px;top:180px">
    <svg width="90" height="66" viewBox="0 0 90 66" fill="none" stroke="#1d6f72" stroke-width="2.5"><circle cx="45" cy="14" r="10"/><circle cx="20" cy="30" r="8"/><circle cx="70" cy="30" r="8"/><path d="M30 60V40c0-8 6-12 15-12s15 4 15 12v20"/><path d="M6 60V50c0-6 6-10 14-10 4 0 7 1 10 3"/><path d="M84 60V50c0-6-6-10-14-10-4 0-7 1-10 3"/><path d="M4 62h82"/></svg>
    <h3>Guest Relations</h3><p>Maecenas vel tortor accumsan quam varius imperdiet vel eget elit</p></div>

  <div class="btn" style="top:384px;left:538px;width:124px;height:41px">Book Now</div>
</section>

<div class="vline" style="top:1735px;height:61px"></div>
<h2 class="abs heading" style="top:1818px"><b>TESTIMONIALS</b></h2>
<svg class="abs" style="top:1912px;left:48px" width="18" height="28" viewBox="0 0 18 28"><path d="M15 2 3 14l12 12" fill="none" stroke="#555" stroke-width="3"/></svg>
<svg class="abs" style="top:1912px;left:1133px" width="18" height="28" viewBox="0 0 18 28"><path d="M3 2l12 12L3 26" fill="none" stroke="#555" stroke-width="3"/></svg>
<p class="abs quote">" Etiam mattis augue vehicula odio posuere, sit amet tempus lectus luctus. Nulla facilisi. Etiam vel massa elementum, bibendum tellus venenatis, feugiat massa. Curabitur venenatis lacinia ornare. "</p>
<p class="abs author">Daniel Reyes</p>
<div class="abs dots"><i class="on"></i><i></i><i></i></div>

<section class="abs cta" role="img" aria-label="Faded group photo of smiling hospitality staff in uniforms"></section>
<div class="vline" style="top:2144px;height:61px"></div>
<h2 class="abs heading" style="top:2229px"><b>VESTIBULUM</b> <span>CONDIMENTUM</span></h2>
<p class="abs cta-text">Phasellus nisl est, condimentum vitae faucibus in, sollicitudin vel metus. Nunc sit amet consequat risus. Curabitur ac elit leo. In eleifend dui tellus, in scelerisque elit porttitor et. Integer eu massa lacinia, lacinia nulla non, volutpat purus.</p>
<div class="btn" style="top:2406px;left:538px;width:124px;height:41px">Contact Us</div>
<div class="abs socials"><i></i><i></i><i></i><i></i><i></i></div>

<footer class="abs site-footer">
  <div class="abs footer-brand"><span class="dot"></span><span class="brand-name">BrightVoyage</span></div>
  <div class="abs divider" style="left:366px"></div>
  <div class="abs contacts" style="top:32px;left:478px">Mexico - +52 55 0100 4821<br>Europe - +33 7 0100 2946<br>US - +1 307-555-0187</div>
  <div class="abs divider" style="left:747px"></div>
  <div class="abs contacts" style="top:32px;left:859px">Australia - +61 402 555 019<br>Email - info@brightvoyage-intern.example</div>
  <p class="abs copyright">Copyright © 2018 BrightVoyage. All rights reserved.</p>
  <div class="abs chat"><span>CHAT WITH US!</span><svg width="14" height="9" viewBox="0 0 14 9"><path d="M1 8l6-6 6 6" fill="none" stroke="#fff" stroke-width="2.5"/></svg></div>
  <span class="abs chat-tag">M2</span>
</footer>

</body>
</html>
```